Calder Pizza - Takeout Menu Design

We are looking for a takeout menu design.
We are looking for a( 5" x 8.5" DOUBLE SIDED) flyer with our available pizza flavors
Must be easy to ready and not "busy"

Must include our logo (attached)
website: www.calderpizza.ca
address:
Fenwick Ridge Plaza
417, 318 9 Avenue SW
and the following details:
Visit our website for our complete appetizer, pasta, salad and catering menu.

Winner of this contest will also be offered to create a few print designs via printhive.

Please do not hesitate to ask any questions.

Target Market(s)

Business / Office clientele

Industry/Entity Type

Pizza place / specializing in corporate orders

Requirements
Must have
• Easy to read
Should not have
• Can not be busy or cluttered

```html
<!DOCTYPE html>
<html lang="en">
<head>
<meta charset="utf-8">
<title>Calder Pizza – Take-Out Menu</title>
<link rel="stylesheet" href="https://fonts.googleapis.com/css2?family=Montserrat:wght@400;500;600&family=Open+Sans:ital,wght@0,400;0,600;1,400&display=swap">
<style>
  :root {
    --backdrop: #d7d1fd;
    --paper: #ffffff;
    --brand-red: #c0311f;
    --ribbon: #1e1e1e;
    --ribbon-dark: #3a3a3a;
    --ink: #1f1f1f;
    --muted: #3d3d3d;
    --tile: #f9e6e4;
    --panel: #efefef;
    --panel-art: #e2e2e2;
  }
  * { box-sizing: border-box; margin: 0; padding: 0; }
  html, body { width: 1200px; height: 948px; overflow: hidden; background: var(--backdrop); }
  .stage {
    position: relative; width: 1404px; height: 1109px;
    transform: scale(0.8547); transform-origin: 0 0;
    font-family: "Open Sans", Arial, sans-serif; color: var(--ink);
  }
  .page { position: absolute; top: 146px; width: 480px; height: 816px; background: var(--paper); }
  .page--front { left: 189px; }
  .page--back { left: 734px; }
  .page > * { position: absolute; }

  .brand-band { background: var(--brand-red); color: #fff; display: flex; flex-direction: column; align-items: center; justify-content: center; }
  .brand-name { font-family: "Open Sans", Arial, sans-serif; font-weight: 600; font-size: 26px; line-height: 1; }

  .ribbon {
    background: var(--ribbon); color: #fff; height: 28px; width: 264px;
    font-family: "Montserrat", sans-serif; font-weight: 600; font-size: 12.5px;
    display: flex; align-items: center; justify-content: center;
    clip-path: polygon(0 0, 100% 0, 96.5% 50%, 100% 100%, 0 100%, 3.5% 50%);
  }

  .sizes { display: grid; grid-template-columns: 43px 43px; font-style: italic; font-size: 8.5px; }

  .row { display: grid; grid-template-columns: 121px 43px 43px; font-size: 10px; line-height: 13px; }
  .price { font-size: 10px; line-height: 10px; }

  .item { display: grid; grid-template-columns: 121px 43px 43px; align-items: start; }
  .item h3 { grid-column: 1 / -1; font-weight: 600; font-size: 10.5px; line-height: 13px; }
  .item p { font-size: 7.5px; line-height: 10px; margin-top: 3px; color: var(--muted); padding-right: 4px; }
  .item .price { margin-top: 3px; }
  .item .note { display: block; font-style: italic; font-size: 7px; color: #777; line-height: 10px; grid-column: 2 / -1; }

  .fine { font-style: italic; font-size: 7.5px; text-align: center; color: var(--muted); }

  .feature-box { background: var(--panel); }
  .art { background: var(--panel-art); border-radius: 6px; }

  .tiles { display: flex; gap: 5px; }
  .tile { width: 80px; height: 94px; background: var(--tile); display: flex; flex-direction: column; align-items: center; }
  .tile .art { width: 40px; height: 40px; margin-top: 15px; background: #e8cfcc; border-radius: 50%; }
  .tile span { margin-top: 20px; font-size: 10px; font-weight: 600; }

  .catering { background: var(--panel); }
  .catering .art { position: absolute; left: 58px; top: 12px; width: 50px; height: 50px; background: #d9d9d9; }
  .catering .ribbon { position: absolute; left: 20px; top: 68px; width: 130px; background: var(--ribbon-dark); font-size: 12px; }
  .catering .copy { position: absolute; left: 186px; top: 20px; width: 215px; font-size: 7.5px; line-height: 10px; }
  .catering .copy em { display: block; margin-top: 6px; }

  .address { font-weight: 600; font-size: 10px; margin-top: 14px; }
  .site { font-size: 10px; margin-top: 12px; }
  .fold { width: 24px; height: 24px; background: var(--tile); clip-path: polygon(0 100%, 100% 0, 100% 100%); }
</style>
</head>
<body>
<div class="stage">

  <section class="page page--front">
    <header class="brand-band" style="left:31px;top:0;width:418px;height:64px;">
      <span class="brand-name">Calder Pizza</span>
    </header>

    <div class="ribbon" style="left:108px;top:92px;">Classic Take-Out Pizza 8” &amp; 13”</div>

    <div class="sizes" style="left:152px;top:133px;"><span>8”</span><span>13”</span></div>
    <div class="sizes" style="left:374px;top:133px;"><span>8”</span><span>13”</span></div>

    <div class="row" style="left:30px;top:152px;"><span>Pepperoni &amp; Mushroom</span><span>$12.99</span><span>$30.95</span></div>
    <div class="row" style="left:30px;top:177px;"><span>Pepperoni</span><span>$11.99</span><span>$29.95</span></div>
    <div class="row" style="left:30px;top:202px;"><span>Hawaiian</span><span>$12.99</span><span>$30.95</span></div>
    <div class="row" style="left:30px;top:227px;"><span>Beef &amp; Mushroom</span><span>$13.49</span><span>$32.95</span></div>

    <div class="row" style="left:253px;top:154px;"><span>Pepperoni &amp; Ham</span><span>$12.99</span><span>$30.95</span></div>
    <div class="row" style="left:253px;top:179px;"><span>Ham &amp; Mushroom</span><span>$12.99</span><span>$30.95</span></div>
    <div class="row" style="left:253px;top:204px;"><span>Beef &amp; Onion</span><span>$13.49</span><span>$32.95</span></div>
    <div class="row" style="left:253px;top:229px;"><span>Cheese</span><span>$11.99</span><span>$29.95</span></div>

    <div class="ribbon" style="left:108px;top:270px;">Specialty Take-Out Pizza 8” &amp; 13”</div>

    <div class="sizes" style="left:152px;top:319px;"><span>8”</span><span>13”</span></div>
    <div class="sizes" style="left:374px;top:319px;"><span>8”</span><span>13”</span></div>

    <div class="item" style="left:31px;top:316px;"><h3>All Meat</h3><p>Pepperoni, Beef &amp; Smoked Ham &amp; Bacon</p><span class="price">$14.99</span><span class="price">$35.95</span></div>
    <div class="item" style="left:31px;top:362px;"><h3>Double Pepperoni</h3><p>Loads of Pepperoni</p><span class="price">$13.49</span><span class="price">$32.95</span></div>
    <div class="item" style="left:31px;top:398px;"><h3>Hot Honey Pepperoni</h3><p>Double Pepperoni and drizzled with Hot Honey</p><span class="price">$14.49</span><span class="price">$34.95</span></div>
    <div class="item" style="left:31px;top:444px;"><h3>Hawaiian Heat</h3><p>Smoked Ham, Pineapple and Banana Peppers</p><span class="price">$13.49</span><span class="price">$32.95</span></div>
    <div class="item" style="left:31px;top:492px;"><h3>Four Cheese</h3><p>Mozzarella, Feta, Romano and Cheddar Cheese</p><span class="price">$13.49</span><span class="price">$32.95</span></div>
    <div class="item" style="left:31px;top:540px;"><h3>Montreal</h3><p>Pepperoni &amp; Double Smoked Bacon</p><span class="price">$13.49</span><span class="price">$32.95</span></div>
    <div class="item" style="left:31px;top:588px;"><h3>Montreal Heat</h3><p>Pepperoni, Double Smoked Bacon &amp; Banana Peppers</p><span class="price">$13.99</span><span class="price">$33.95</span></div>
    <div class="item" style="left:31px;top:636px;"><h3>Supreme</h3><p>Pepperoni, Mushrooms &amp; Green Peppers</p><span class="price">$13.49</span><span class="price">$32.95</span></div>
    <div class="item" style="left:31px;top:682px;"><h3>Canadian</h3><p>Pepperoni, Mushrooms &amp; Ham</p><span class="price">$13.49</span><span class="price">$32.95</span></div>
    <div class="item" style="left:31px;top:720px;"><h3>BBQ Chicken</h3><p>Chicken Breast, Hickory BBQ Sauce &amp; Red Onions.</p><span class="price">$13.99</span><span class="price">$33.95</span></div>

    <div class="item" style="left:253px;top:316px;"><h3>BBQ Chicken Plus</h3><p>Chicken Breast, Hickory BBQ Sauce, Red Onions &amp; Cilantro</p><span class="price">$14.79</span><span class="price">$34.95</span></div>
    <div class="item" style="left:253px;top:362px;"><h3>Spicy BBQ Chicken</h3><p>Chicken Breast, Hickory BBQ Sauce, Red Onions &amp; Banana Peppers</p><span class="price">$14.49</span><span class="price">$35.95</span></div>
    <div class="item" style="left:253px;top:418px;"><h3>Sweet Chili Chicken</h3><p>Chicken Breast, Pineapple, Red Onions &amp; Sweet Chili Sauce</p><span class="price">$14.49</span><span class="price">$35.95</span></div>
    <div class="item" style="left:253px;top:475px;"><h3>Chicken Club</h3><p>Chicken Breast, Double Smoked Bacon, Red Onions and Tomatoes</p><span class="price">$14.79</span><span class="price">$35.95</span></div>
    <div class="item" style="left:253px;top:531px;"><h3>Athenean</h3><p>Chicken Breast, Spinach, Feta Cheese and Tomato</p><span class="price">$14.49</span><span class="price">$34.95</span></div>
    <div class="item" style="left:253px;top:579px;"><h3>Greek Supreme</h3><p>Chicken Breast, Feta Cheese, Tomato, Green Pepper, Red Onions &amp; Black Olives</p><span class="price">$14.99</span><span class="price">$35.95</span></div>
    <div class="item" style="left:253px;top:635px;"><h3>Mediterranean Chicken</h3><p>Seasoned Chicken Breast, Tomatoes, Red Onions and Feta Cheese</p><span class="price">$14.79</span><span class="price">$35.95</span></div>
    <div class="item" style="left:253px;top:692px;"><h3>Original Spinach</h3><p>Spinach &amp; Feta Cheese</p><span class="price">$13.49</span><span class="price">$32.95</span></div>
    <div class="item" style="left:253px;top:730px;"><h3>Zeus</h3><p>Spinach, Feta Cheese and Tomatoes</p><span class="price">$13.95</span><span class="price">$33.95</span></div>

    <p class="fine" style="left:0;top:787px;width:480px;">All of our pizzas are prepared fresh everyday using only the finest mozzarella blend and ingredients.</p>
    <div class="fold" style="left:456px;top:792px;"></div>
  </section>

  <section class="page page--back">
    <div class="ribbon" style="left:109px;top:44px;">Specialty Take-Out Pizza 8” &amp; 13”</div>

    <div class="sizes" style="left:152px;top:91px;"><span>8”</span><span>13”</span></div>
    <div class="sizes" style="left:374px;top:91px;"><span>8”</span><span>13”</span></div>

    <div class="item" style="left:31px;top:89px;"><h3>Greek</h3><p>Feta Cheese, Tomato, Green Peppers, Red Onions and Black Olives</p><span class="price">$13.99</span><span class="price">$33.95</span></div>
    <div class="item" style="left:31px;top:145px;"><h3>Vegetarian</h3><p>Mushrooms, Tomatoes, Green Peppers and Black Olives</p><span class="price">$13.49</span><span class="price">$32.95</span></div>
    <div class="item" style="left:31px;top:201px;"><h3>Veggie Delight</h3><p>Mushrooms, Tomatoes, Green Peppers, Black Olives &amp; Onions</p><span class="price">$13.95</span><span class="price">$33.95</span></div>
    <div class="item" style="left:31px;top:258px;"><h3>Deluxe</h3><p>Pepperoni, Mushrooms, Ham, Tomatoes, Green Peppers and Red Onions</p><span class="price">$14.49</span><span class="price">$34.95</span></div>

    <div class="item" style="left:253px;top:89px;"><h3>Calder Special</h3><p>Pepperoni, Mushrooms, Ham, Green Peppers and Black Olives</p><span class="price">$14.49</span><span class="price">$34.95</span></div>
    <div class="item" style="left:253px;top:146px;">
      <h3>Dill Pickle</h3>
      <p style="grid-row: span 3;">Crispy Dill Pickles, Fresh Dill with our cream based garlic sauce.</p>
      <span class="price">$13.49</span><span class="price">$32.95</span>
      <span class="note">(with our bacon)</span>
      <span class="price" style="grid-column:2;margin-top:5px;">$14.49</span><span class="price" style="margin-top:5px;">$35.95</span>
    </div>
    <span style="position:absolute;left:374px;top:203px;font-style:italic;font-size:7px;color:#777;">(without our bacon)</span>

    <div class="feature-box" style="left:253px;top:223px;width:196px;height:83px;">
      <div class="art" role="img" aria-label="Faint grill icon" style="position:absolute;left:122px;top:8px;width:60px;height:66px;opacity:.45;"></div>
      <div class="item" style="position:absolute;left:6px;top:12px;grid-template-columns:109px 43px 43px;">
        <h3>BBQ Pulled Pork</h3><p>Pulled Pork, Red Onions, Red Peppers and Cilantro.</p><span class="price" style="margin-top:4px;">$14.49</span><span class="price" style="margin-top:4px;">$35.95</span>
      </div>
    </div>

    <div class="ribbon" style="left:109px;top:350px;">You can try other menu items</div>

    <div class="tiles" style="left:32px;top:407px;">
      <div class="tile"><div class="art" role="img" aria-label="Appetizer skewers icon"></div><span>Appetizers</span></div>
      <div class="tile"><div class="art" role="img" aria-label="Pasta bowl icon"></div><span>Pasta</span></div>
      <div class="tile"><div class="art" role="img" aria-label="Salad bowl icon"></div><span>Salad</span></div>
      <div class="tile"><div class="art" role="img" aria-label="Beverage bottles icon"></div><span>Beverages</span></div>
      <div class="tile"><div class="art" role="img" aria-label="Gluten free icon"></div><span>Gluten Smart</span></div>
    </div>

    <div class="catering" style="left:32px;top:526px;width:417px;height:112px;">
      <div class="art" role="img" aria-label="Chef serving a catering table"></div>
      <div class="ribbon">Catering</div>
      <div class="copy">
        Calder offers a wide selection of gourmet pizza, pasta, salads and appetizers for functions of any size or for any occasion! We specialize in office parties!
        <em>Contact us to learn more about our catering menu, or if you need something specific please contact us about custom catering orders.</em>
      </div>
    </div>

    <p class="fine" style="left:0;top:655px;width:480px;font-size:7px;">GST not Included</p>
    <p class="fine" style="left:0;top:672px;width:480px;">All of our pizzas are prepared fresh everyday using only the finest mozzarella blend and ingredients.</p>

    <footer class="brand-band" style="left:32px;top:693px;width:417px;height:123px;">
      <span class="brand-name">Calder Pizza</span>
      <p class="address">Fenwick Ridge Plaza 417, 318 9 Avenue SW</p>
      <p class="site">www.calderpizza.ca</p>
    </footer>
  </section>

</div>
</body>
</html>
```